Lubricants Company | ||
Company Profile and Marketing | ||
TORVANE Lubricants Manufacturer located in Dammam. The plant will be in process in 2013. This company profile will be used to give an introduction about our plant and company's strategy. Also, another main objective is to be used for a marketing purpose for the plant from the time being. |
Corporate | ||
Professional looking comapny profile that will provide an introduction and a marketing purpose in order to provide business opportunities for future (when plant is in process). | ||

```html
<!DOCTYPE html>
<html lang="en">
<head>
<meta charset="utf-8">
<title>TORVANE Corporate Profile</title>
<link rel="stylesheet" href="https://fonts.googleapis.com/css2?family=Lato:wght@400;700&family=Raleway:wght@300;500;700&display=swap">
<style>
  :root{
    --bg:#e9e6e1;
    --paper:#ffffff;
    --navy:#1d3f8f;
    --blue:#2a6bc2;
    --sky:#3c8fe0;
    --ink:#4a4f57;
    --grey:#c9ccd2;
    --shadow:0 4px 12px rgba(0,0,0,.25);
  }
  *{box-sizing:border-box;margin:0;padding:0}
  html,body{width:1200px;height:874px;overflow:hidden;background:var(--bg)}
  body{position:relative;font-family:"Lato",sans-serif;color:var(--ink)}
  .page{position:absolute;background:var(--paper);box-shadow:var(--shadow);overflow:hidden}
  .spread{display:flex}
  .spread .half{position:relative;width:50%;height:100%;overflow:hidden}
  .spread .half + .half{border-left:1px solid #e3e5ea}
  .band{position:absolute;left:0;right:0;bottom:0;height:8px;background:linear-gradient(90deg,var(--navy),var(--sky))}
  .band.top{top:0;bottom:auto;height:6px}
  .photo{position:absolute;inset:0}
  h2{font-family:"Raleway",sans-serif;font-weight:700;color:var(--navy);font-size:11px;margin-bottom:6px}
  p{font-size:6.5px;line-height:1.45;margin-bottom:6px}
  .text{position:absolute;padding:18px 16px}
  .brand{display:flex;align-items:center;gap:6px;font-family:"Raleway",sans-serif;font-weight:700;color:var(--navy);letter-spacing:1px}
  .brand .dot{width:12px;height:12px;border-radius:50%;background:var(--blue)}

  /* front cover */
  .cover{left:36px;top:108px;width:192px;height:252px}
  .cover .pattern{position:absolute;right:0;top:0;width:150px;height:150px;background:linear-gradient(225deg,#d4d7dd,#f3f4f6 70%)}
  .cover .brand{position:absolute;left:28px;top:150px;font-size:13px}
  .cover .title{position:absolute;left:28px;top:178px;font-family:"Raleway",sans-serif;font-weight:500;font-size:10px;letter-spacing:1px;color:var(--navy);border-top:1px solid var(--navy);padding-top:4px}

  /* envision spread */
  .envision{left:252px;top:108px;width:330px;height:252px}
  .envision .photo{background:linear-gradient(180deg,#2a3e8e 0%,#5a63b8 35%,#8a6aa6 55%,#2b3550 75%,#121a2c 100%)}
  .envision .headline{position:absolute;left:24px;top:26px;color:#fff;font-family:"Raleway",sans-serif;font-weight:300;line-height:1}
  .envision .headline .small{display:block;font-size:18px;letter-spacing:1px}
  .envision .headline .big{display:block;font-size:42px;letter-spacing:2px}

  /* strategy spread */
  .strategy{left:600px;top:72px;width:360px;height:230px}
  .strategy .photo{background:radial-gradient(circle at 55% 55%,#f3c24a,#c98a12 45%,#5a4a33 75%,#2b2a28)}

  /* profile spread */
  .profile{left:240px;top:390px;width:336px;height:222px}
  .profile .photo{background:linear-gradient(160deg,#d7c3a2,#9b7a55 55%,#4a3a2c)}

  /* products spread */
  .products{left:612px;top:322px;width:340px;height:222px}
  .products .photo{background:linear-gradient(135deg,#8ea3c0,#3b4a60 50%,#1f2633)}

  /* sustainability spread */
  .sustain{left:596px;top:566px;width:340px;height:262px;background:var(--navy)}
  .sustain .half{background:linear-gradient(160deg,#2e61b6,#183f85)}
  .sustain h2{color:#fff}
  .sustain p{color:#dce6f7}
  .sustain .photo{background:linear-gradient(180deg,#4f8fd8,#1d4b97 70%,#133671)}

  /* back cover */
  .back{left:996px;top:504px;width:156px;height:252px}
  .back .pattern{position:absolute;left:0;top:0;width:156px;height:130px;background:linear-gradient(200deg,#d4d7dd,#f6f7f8 75%)}
  .back .brand{position:absolute;left:46px;top:140px;font-size:10px}
  .back .contact{position:absolute;left:46px;top:162px;font-size:6px;line-height:1.6}
</style>
</head>
<body>

<section class="page cover">
  <div class="pattern" role="img" aria-label="Faint grey square pattern"></div>
  <div class="brand"><span class="dot"></span>TORVANE</div>
  <div class="title">CORPORATE PROFILE</div>
  <div class="band"></div>
</section>

<section class="page envision">
  <div class="photo" role="img" aria-label="Refinery plant lit at dusk under a purple sky"></div>
  <div class="headline"><span class="small">ENVISIONING A BRIGHTER</span><span class="big">TOMORROW</span></div>
</section>

<section class="page spread strategy">
  <div class="half"><div class="photo" role="img" aria-label="Golden oil pouring from a container"></div></div>
  <div class="half">
    <div class="band top"></div>
    <div class="text">
      <h2>Our Strategy</h2>
      <p>We build a modern blending plant in Dammam that serves regional industry with reliable lubricants and steady supply.</p>
      <p>Quality control, skilled people and efficient logistics guide every step from base oil to finished product.</p>
    </div>
    <div class="band"></div>
  </div>
</section>

<section class="page spread profile">
  <div class="half">
    <div class="band top"></div>
    <div class="text">
      <h2>Company Profile</h2>
      <p>TORVANE is a lubricants manufacturer based in Dammam, preparing a new plant to start production in 2013.</p>
    </div>
    <div class="band"></div>
  </div>
  <div class="half">
    <div class="photo" role="img" aria-label="Businessman seated in a modern office lounge"></div>
    <div class="text" style="left:0;top:30px;width:95px;background:rgba(255,255,255,.92);padding:10px">
      <h2>Our Vision</h2>
      <p>To be the trusted regional name in high quality lubricants.</p>
      <h2>Our Mission</h2>
      <p>To deliver dependable products, service and value to every customer.</p>
    </div>
    <div class="band"></div>
  </div>
</section>

<section class="page spread products">
  <div class="half">
    <div class="band top"></div>
    <div class="text">
      <h2>Products</h2>
      <p>Our range covers engine oils, gear oils, hydraulic fluids and greases for automotive and industrial use.</p>
      <p>Each grade is blended to meet international standards and tested in our own laboratory.</p>
    </div>
    <div class="band"></div>
  </div>
  <div class="half"><div class="photo" role="img" aria-label="Mechanic working on a car engine"></div></div>
</section>

<section class="page spread sustain">
  <div class="half">
    <div class="text">
      <h2>Business Sustainability</h2>
      <p>We plan for long term growth through safe operations, careful use of resources and local partnerships.</p>
      <p>Our plant is designed to reduce waste and energy use while supporting the community.</p>
    </div>
  </div>
  <div class="half"><div class="photo" role="img" aria-label="Construction crane beside a glass tower against a blue sky"></div></div>
</section>

<section class="page back">
  <div class="pattern" role="img" aria-label="Faint grey square pattern"></div>
  <div class="brand"><span class="dot" style="width:9px;height:9px"></span>TORVANE</div>
  <div class="contact">Dammam, Kingdom of Saudi Arabia<br>P.O. Box 0000<br>Tel: +966 13 000 0000<br>info@torvane.example</div>
  <div class="band"></div>
</section>

</body>
</html>
```